New business card for civil engineering company - "Keystone Audit"

We need a business card designed for our new structural engineering company.

The company name is "Keystone Audit" logo files attached.

We would like the following:
* Two-sided card
* Simple design

Information to be placed on the card:
Name - Marcus Dellow
Job Title - Director / Structural Engineer
Credentials - BEng(Hons), CPEng, CMengNZ, IntPE(NZ)
Email - marcus.dellow@keystoneaudit.co.nz
mobile - 0219364058
website - www.keystoneaudit.co.nz

```html
<!DOCTYPE html>
<html lang="en">
<head>
<meta charset="UTF-8">
<title>Keystone Audit – Business Card</title>
<link href="https://fonts.googleapis.com/css2?family=Montserrat:wght@400;500;700&display=swap" rel="stylesheet">
<style>
  :root {
    --stage: #34323a;
    --card: #ffffff;
    --navy: #0d4272;
    --sky: #6ec8ee;
    --blue: #2d86cf;
    --mark-front: #2a78bf;
    --mark-back: #9fd0f0;
    --icon: #2f8fd4;
    --ink: #3a3a3a;
    --muted: #6d6d6d;
  }
  html, body {
    margin: 0;
    width: 1200px;
    height: 900px;
    overflow: hidden;
    background: var(--stage);
    font-family: "Montserrat", Arial, sans-serif;
  }
  .canvas {
    position: relative;
    width: 1200px;
    height: 900px;
  }
  .card {
    position: absolute;
    left: 293px;
    width: 613px;
    height: 350px;
    display: block;
  }
  .card--front { top: 63px; }
  .card--back { top: 485px; }
  .fill-card { fill: var(--card); }
  .fill-navy { fill: var(--navy); }
  .fill-sky { fill: var(--sky); }
  .fill-blue { fill: var(--blue); }
  .fill-icon { fill: var(--icon); }
  .brand-mark--front { fill: var(--mark-front); }
  .brand-mark--back { fill: var(--mark-back); }
  .holder-name { fill: var(--ink); font-size: 22px; font-weight: 500; }
  .credentials { fill: var(--ink); font-size: 5.6px; font-weight: 700; }
  .job-title { fill: var(--ink); font-size: 13px; font-weight: 400; }
  .contact { fill: var(--ink); font-size: 12px; font-weight: 400; }
  .brand-name { fill: #ffffff; font-size: 12.5px; font-weight: 700; letter-spacing: 0.6px; }
  .brand-tagline { fill: #ffffff; font-size: 5.2px; font-weight: 500; letter-spacing: 1.2px; }
  .back-brand { fill: var(--ink); font-size: 17px; font-weight: 700; letter-spacing: 1px; }
  .back-tagline { fill: var(--muted); font-size: 6.4px; font-weight: 500; letter-spacing: 1.7px; }
  .back-web { fill: var(--muted); font-size: 8px; font-weight: 400; }
</style>
</head>
<body>
<main class="canvas">

  <svg class="card card--front" viewBox="0 0 469 268" aria-label="Business card front">
    <defs>
      <clipPath id="front-shape"><rect width="469" height="268" rx="14"/></clipPath>
    </defs>
    <g clip-path="url(#front-shape)">
      <rect class="fill-card" width="469" height="268"/>
      <polygon class="fill-sky" points="436,0 469,0 469,268 0,268 0,257 229,257"/>
      <polygon class="fill-navy" points="449,0 469,0 469,268 236,268"/>
    </g>

    <text class="holder-name" x="23" y="85">Marcus Dellow
      <tspan class="credentials" dx="4">BEng(Hons), CPEng, CMengNZ, IntPE(NZ)</tspan>
    </text>
    <text class="job-title" x="33" y="107">Director | Structural Engineer</text>

    <g class="contact-list">
      <circle class="fill-icon" cx="38" cy="148" r="6"/>
      <rect x="35.6" y="144.2" width="4.8" height="7.6" rx="1" fill="none" stroke="#fff" stroke-width="1.1"/>
      <text class="contact" x="58" y="152.5">0219364058</text>

      <circle class="fill-icon" cx="38" cy="171" r="6"/>
      <rect x="34.7" y="168.6" width="6.6" height="4.8" rx="0.8" fill="#fff"/>
      <text class="contact" x="58" y="175.5">marcus.dellow@keystoneaudit.co.nz</text>

      <circle class="fill-icon" cx="38" cy="194" r="6"/>
      <circle cx="38" cy="194" r="3.4" fill="none" stroke="#fff" stroke-width="1.1"/>
      <text class="contact" x="58" y="198.5">www.keystoneaudit.co.nz</text>
    </g>

    <g class="brand-lockup">
      <rect class="brand-mark--front" x="354" y="160" width="40" height="40" aria-hidden="true"/>
      <text class="brand-name" x="453" y="238" text-anchor="end">KEYSTONE AUDIT</text>
      <text class="brand-tagline" x="453" y="248" text-anchor="end">PEER REVIEW SPECIALISTS</text>
    </g>
  </svg>

  <svg class="card card--back" viewBox="0 0 469 268" aria-label="Business card back">
    <defs>
      <clipPath id="back-shape"><rect width="469" height="268" rx="14"/></clipPath>
    </defs>
    <g clip-path="url(#back-shape)">
      <rect class="fill-card" width="469" height="268"/>
      <polygon class="fill-sky" points="0,257 238,257 230,268 0,268"/>
      <polygon class="fill-blue" points="244,257 469,257 469,268 236,268"/>
    </g>

    <g class="brand-lockup">
      <rect class="brand-mark--back" x="196.5" y="86" width="76" height="76" aria-hidden="true"/>
      <text class="back-brand" x="234.5" y="191" text-anchor="middle">KEYSTONE AUDIT</text>
      <text class="back-tagline" x="234.5" y="204" text-anchor="middle">PEER REVIEW SPECIALISTS</text>
    </g>

    <g class="web">
      <circle cx="179" cy="223" r="3.6" fill="none" stroke="var(--icon)" stroke-width="1.8"/>
      <text class="back-web" x="188" y="226">www.keystoneaudit.co.nz</text>
    </g>
  </svg>

</main>
</body>
</html>
```